Fishing charter business in Sitka Alaska needs new business card design

I have had the same design for 10 plus years, ready for something different. I have attached a copy of my current card and my website link is www.bluecoveangling.net
I am looking for something that will catch my clients eye, although I rely on word of mouth for most of my business a a nice business card will help people remember who I am. My business is located in Sitka Alaska, there are probably 20-30 other charter businesses in Sitka. I like the way my current card is laid out, with the two tone black and grey. I can leave it up to the designers to come up with something else.
Target Market(s)
men, women, couples. Anyone who likes fishing
Industry/Entity Type
Tourism
Contact Information for Business Card
Dorrance's Charter Service
Tidewater Rockline Sportfishing
Colors
Designer to choose colors to be used in the design.
Requirements
Must have
- Gilbert Dorrance
- PO Box 4716
- Sitka, AK 99835
- Compass Rose image
- 100 Ton USCG Licensed Captain
- gdorrance@wavelink.net
- 907-555-0142
- www.bluecoveangling.net
Nice to have
- ghost image of "boat helm"
Should not have
- be to complex

```html
<!DOCTYPE html>
<html lang="en">
<head>
<meta charset="utf-8">
<title>Gilbert Dorrance – Business Card</title>
<link rel="stylesheet" href="https://fonts.googleapis.com/css2?family=Bebas+Neue&family=Lato:wght@400&display=swap">
<style>
  :root {
    --page-bg: #e6ebee;
    --card-top: #6fa3a8;
    --card-bottom: #5e9196;
    --name-ink: #3a3d40;
    --title-red: #d9472f;
    --contact-ink: #3f4a4d;
    --icon-red: #c9473a;
    --ghost-white: rgba(255, 255, 255, 0.75);
    --compass-light: #c9d3ee;
    --compass-mid: #7f90c4;
    --compass-dark: #2b3150;
  }
  * { margin: 0; padding: 0; box-sizing: border-box; }
  html, body {
    width: 1200px;
    height: 900px;
    overflow: hidden;
    background: var(--page-bg);
  }
  .canvas {
    position: relative;
    width: 1200px;
    height: 900px;
  }
  .business-card {
    position: absolute;
    left: 150px;
    top: 193px;
    width: 900px;
    height: 513px;
    background: linear-gradient(160deg, var(--card-top), var(--card-bottom));
    box-shadow: 0 10px 30px rgba(40, 60, 70, 0.18);
    overflow: hidden;
  }
  .captain-name {
    position: absolute;
    left: 58px;
    top: 78px;
    font-family: "Bebas Neue", "Oswald", sans-serif;
    font-size: 42px;
    letter-spacing: 1.5px;
    line-height: 1;
    color: var(--name-ink);
    font-weight: 400;
  }
  .captain-license {
    position: absolute;
    left: 58px;
    top: 122px;
    font-family: "Lato", sans-serif;
    font-size: 18px;
    color: var(--title-red);
  }
  .helm-ghost {
    position: absolute;
    left: 60px;
    top: 160px;
    width: 150px;
    height: 150px;
  }
  .contact-list {
    position: absolute;
    left: 58px;
    top: 362px;
    list-style: none;
    font-family: "Lato", sans-serif;
    font-size: 18px;
    line-height: 22px;
    color: var(--contact-ink);
  }
  .contact-list li {
    display: flex;
    align-items: center;
    gap: 10px;
  }
  .contact-icon {
    width: 13px;
    height: 13px;
    flex: none;
  }
  .compass-rose {
    position: absolute;
    left: 456px;
    top: 86px;
    width: 360px;
    height: 360px;
  }
</style>
</head>
<body>
<main class="canvas">
  <section class="business-card">
    <h1 class="captain-name">Gilbert Dorrance</h1>
    <p class="captain-license">100 Ton USCG Licensed Captain</p>

    <svg class="helm-ghost" viewBox="0 0 150 150" role="img" aria-label="Faint ship's helm wheel ghost image">
      <defs>
        <radialGradient id="helm-glow" cx="50%" cy="50%" r="50%">
          <stop offset="0%" stop-color="#ffffff" stop-opacity="0.55"/>
          <stop offset="70%" stop-color="#ffffff" stop-opacity="0.3"/>
          <stop offset="100%" stop-color="#ffffff" stop-opacity="0"/>
        </radialGradient>
      </defs>
      <circle cx="75" cy="75" r="75" fill="url(#helm-glow)"/>
    </svg>

    <ul class="contact-list">
      <li>
        <svg class="contact-icon" viewBox="0 0 16 16"><path fill="var(--icon-red)" d="M3 1l3 3-1.5 2a9 9 0 0 0 5.5 5.5L12 10l3 3-2 2C7 15 1 9 1 3z"/></svg>
        +907-555-0142
      </li>
      <li>
        <svg class="contact-icon" viewBox="0 0 16 16"><rect x="1" y="3" width="14" height="10" rx="1" fill="var(--icon-red)"/><path d="M1.5 4l6.5 5 6.5-5" stroke="#fff" stroke-width="1.3" fill="none"/></svg>
        gdorrance@wavelink.net
      </li>
      <li>
        <svg class="contact-icon" viewBox="0 0 16 16"><circle cx="8" cy="8" r="7" fill="var(--icon-red)"/></svg>
        www.bluecoveangling.net
      </li>
      <li>
        <svg class="contact-icon" viewBox="0 0 16 16"><path fill="var(--icon-red)" d="M8 0a5.5 5.5 0 0 0-5.5 5.5C2.5 10 8 16 8 16s5.5-6 5.5-10.5A5.5 5.5 0 0 0 8 0zm0 8a2.5 2.5 0 1 1 0-5 2.5 2.5 0 0 1 0 5z"/></svg>
        P.O. Box 4716. Sitka, AK 99835
      </li>
    </ul>

    <svg class="compass-rose" viewBox="0 0 360 360" role="img" aria-label="Compass rose with eight marked directions">
      <defs>
        <radialGradient id="compass-fill" cx="50%" cy="50%" r="50%">
          <stop offset="0%" stop-color="var(--compass-mid)"/>
          <stop offset="45%" stop-color="var(--compass-light)" stop-opacity="0.9"/>
          <stop offset="75%" stop-color="var(--compass-dark)" stop-opacity="0.35"/>
          <stop offset="100%" stop-color="var(--compass-dark)" stop-opacity="0"/>
        </radialGradient>
      </defs>
      <circle cx="180" cy="180" r="178" fill="url(#compass-fill)"/>
    </svg>
  </section>
</main>
</body>
</html>
```